Form Crafters Business Card

Professional cosmetic surgery company, based in very exclusive area in London. High profiled clientele. Brand is very artistic, modern, state-of-the-art, safe. The best in the business. Celebrity clientele.

Form Crafter’s of London is a brand serving a discriminating and exclusive clientele who value personal service that is both intimate and high end. Our clients choose Form Crafters because of the relationships we share with all of our customers. The clients of Form Crafters have an equal partnership between customers, and very experienced, highly qualified medical professionals. This together provides you with a professional service that keeps you looking good and feeling good. It is a relationship based on honesty, compassion, loyalty and respect.
Form Crafter’s have provided services for internationally recognised celebrities, and other high profiled individuals.

The cards are used for networking at private, exclusive events with VIPs.

Target Market(s)

Professionals
Rich people

Industry/Entity Type

Professional Service

Contact Information for Business Card

Need double sided business card design for 4 people. Back of the business card needs to have contrast background to the front with butterfly watermark with services provided:
Hair Restoration surgery
Hair Loss treatments
Breast surgery
Rhinoplasty
Sonix Liposuction
Fat Grafting
Relaxin & Fillers

Front of the business card needs to be a nice satin black.
with following information:
Tavish Kolendran - name
Chief Executive - Job title

www.formcrafters.co.uk
tavish@formcrafters.co.uk
Phone: +44 (0)207 461 2295
Mobile: +44 (0)7912 548 237

The London Ashcombe Clinic
14 Ashcombe Street | London | W1K 3PQ
Off Tolland Street

All business cards have the same address, phone, website as Tavish's details.
Same details on the back of the business card as well.
The other cards have different name, job title, email, mobile number

Faraz Qureshi - Name
Partner - Job Title
Former England International Cricketer - please include below job title

email: faraz@formcrafters.co.uk
mobile: +44(0)7846 205318

Dr Tadeu Varella - Name
Plastic Surgeon - Job Title
drvarella@formcrafters.co.uk
No mobile number

Dr Zain Hussaini FRCS (please put FRCS in small font) - Name
Hair Restoration Surgeon - Job Title
drhussaini@formcrafters.co.uk
No mobile number

Colors
cedeec
85abd2
0655a3

Requirements
Must have
• The logo needs to be in a metallic finish
• Text needs to be striking
• nice background
• butterfly watermark on the back

```html
<!DOCTYPE html>
<html lang="en">
<head>
<meta charset="utf-8">
<title>Form Crafters Business Card</title>
<link href="https://fonts.googleapis.com/css2?family=Lato:wght@400;700&display=swap" rel="stylesheet">
<style>
  :root {
    --page: #d9d9d9;
    --card-black: #050505;
    --white: #ffffff;
    --brand-blue: #1f8fd8;
    --brand-blue-deep: #0655a3;
    --brand-orange: #f28a1e;
    --brand-amber: #f6a821;
    --ornament: #e9731f;
  }
  * { margin: 0; padding: 0; box-sizing: border-box; }
  html, body { width: 1200px; height: 926px; overflow: hidden; }
  body {
    background: var(--page);
    font-family: "Lato", Arial, sans-serif;
    position: relative;
  }
  .card {
    position: absolute;
    top: 314px;
    width: 520px;
    height: 297px;
    background: var(--card-black);
    overflow: hidden;
    box-shadow: 0 6px 18px rgba(0,0,0,0.25);
  }
  .card--front { left: 60px; }
  .card--back { left: 620px; }

  /* Front */
  .brand {
    position: absolute;
    left: 30px;
    top: 28px;
    display: flex;
    align-items: center;
    gap: 10px;
  }
  .brand__dot {
    width: 24px; height: 24px;
    border-radius: 50%;
    background: var(--brand-orange);
  }
  .brand__name {
    font-size: 26px;
    font-weight: 400;
    color: var(--brand-blue);
    letter-spacing: 0.5px;
  }
  .person {
    position: absolute;
    left: 30px;
    top: 84px;
  }
  .person__name {
    font-size: 22px;
    font-weight: 700;
    color: var(--white);
  }
  .person__title {
    font-size: 13px;
    color: var(--brand-amber);
    margin-top: 1px;
  }
  .contact {
    position: absolute;
    left: 30px;
    top: 150px;
    list-style: none;
    font-size: 13.5px;
    line-height: 17.5px;
    color: var(--white);
  }

  /* Back */
  .ornament {
    position: absolute;
    left: 30px;
    top: 0;
    width: 100px;
    height: 80px;
    border-radius: 0 0 60px 10px;
    background: linear-gradient(135deg, var(--brand-blue) 0%, var(--ornament) 70%, var(--brand-amber) 100%);
  }
  .services {
    position: absolute;
    left: 225px;
    top: 52px;
    color: var(--white);
  }
  .services__heading {
    font-size: 12.5px;
    font-weight: 700;
    letter-spacing: 1px;
    padding-bottom: 6px;
    border-bottom: 1px solid var(--white);
    width: 185px;
    margin-bottom: 6px;
  }
  .services__list {
    list-style: none;
    font-size: 13.5px;
    line-height: 16px;
    letter-spacing: 0.4px;
  }
  .accent-bar {
    position: absolute;
    left: 0;
    width: 520px;
  }
  .accent-bar--blue {
    bottom: 46px;
    height: 6px;
    background: linear-gradient(90deg, var(--brand-blue), var(--brand-blue-deep));
  }
  .accent-bar--orange {
    bottom: 0;
    height: 40px;
    background: linear-gradient(90deg, var(--ornament), var(--brand-amber));
  }
</style>
</head>
<body>

<section class="card card--front" aria-label="Business card front">
  <div class="brand">
    <span class="brand__dot"></span>
    <span class="brand__name">Form Crafters</span>
  </div>
  <div class="person">
    <div class="person__name">Tavish Kolendran</div>
    <div class="person__title">Chief Executive</div>
  </div>
  <ul class="contact">
    <li>www.formcrafters.co.uk</li>
    <li>tavish@formcrafters.co.uk</li>
    <li>+44 (0)207 461 2295</li>
    <li>+44 (0)7912 548 237</li>
    <li>The London Ashcombe Clinic</li>
    <li>14 Ashcombe Street , London, W1K 3PQ Off</li>
  </ul>
</section>

<section class="card card--back" aria-label="Business card back">
  <div class="ornament" role="img" aria-label="Butterfly wing ornament in blue and orange"></div>
  <div class="services">
    <div class="services__heading">SERVICES PROVIDED:</div>
    <ul class="services__list">
      <li>Hair Restoration surgery</li>
      <li>Hair Loss treatments</li>
      <li>Breast surgery</li>
      <li>Rhinoplasty</li>
      <li>Sonix Liposuction</li>
      <li>Fat Grafting Relaxin &amp; Fillers</li>
    </ul>
  </div>
  <div class="accent-bar accent-bar--blue"></div>
  <div class="accent-bar accent-bar--orange"></div>
</section>

</body>
</html>
```